Zielgruppe
Wir beraten Menschen aus unterschiedlichen Branchen, die im Rahmen Ihrer Tätigkeit vor einem technologischen Problem bzw. einer technologischen Lücke stehen und helfen diesen über vielfältige Bausteine, um so dem Unternehmen ein Unternehmensupgrade zu verschaffen. Wir schlagen somit eine Brücke zwischen dem Stand von heute in einem Unternehmen zu einem besseren Stand morgen.
Konkret betreiben wir unter anderem externes Projektmanagement, beschaffen Informationen unterschiedlicher Art, vermitteln Kooperationspartner, beraten individuell uvm.
Ob jemand nach einer neuen, innovativen Technologie sucht, Partner benötigt, um eigene Neuentwicklungen voranzutreiben, ein neues Produkt fürs eigene Unternehmen und einen entsprechenden Prototypen sucht, verwendete Stoffe mit anderen ersetzen will - mithilfe unseres weltweiten Expertennetzwerks von über 600.000 direkten Ansprechpartnern finden wir für die meisten Nöte dieser Art eine Lösung bzw. jemanden, der diese lösen kann.
Im Grunde genommen beseitigen wir Engpässe innerhalb von Industrieunternehmen, die beispielsweise sein können
-fehlende TEchnologien/Ersatzprodukte/Ersatzstoffe
-fehlende Ideen für Neuentwicklungen
-fehlendes Wissen im Unternehmen
-fehlende Objektivität hinsichtlich interner Verbesserungsmöglichkeiten
-fehlende Zeit für eigene Projekte, Neuentwicklungen und Suchen versch. Art
Wir finden
- neue Technologien, Ersatzprodukte, Ersatzstoffe
- Ideen für Neuentwicklungen und zusätzlich diejenigen, die dabei unterstützen können
- neue Märkte, um das Unternehmen zu erweitern
- das fehlende Wissen
- den nötigen Abstand, um interne Prozesse und Abläufe objektiv zu beurteilen und geben Vorschläge zur Veränderung/Verbesserung
- passende Realisierungspartner
Wie?
- wir recherchieren (Patente, Literatur) und sammeln Hintergrundwissen
- wir befragen unser Netzwerk und Unternehmen/Wissenschaftler
- wir setzen unsere Töchter..
Aufgabenstellung
Wir benötigen einen faltbaren Flyer, allerdings keinen klassischen, sondern wie ein Theatervorhang. Beispielbilder sind anbei (wir würden die Flyer drucken lassen und dann selbst falten). Wir gehen gerne andere Wege, auch in unseren Projekten.
Der Mensch und dessen Wünsche soll im Mittelpunkt stehen.
Design sollte nicht zu verspielt sein, sich daran orientieren, dass deutsche Unternehmen damit angesprochen werden.
Einen Beispielflyer mit den (noch variablen) Texten ist beigefügt, das Design muss sich nicht daran orientieren. Gute Alternativen sind mehr als gewünscht.
Der Gedanke hinter dem Flyer: Wir schlagen eine Brücke für den Kunden/Menschen zu seinem Ziel. Die Tools, die wir dazu nutzen sind Steine oder wir sprengen den Weg frei zum Ziel o.ä. Auch hier sind Alternativen mehr als willkommen.
Sie dürfen sich so weit wie möglich vom Beispielentwurf und dem Bild der Brücke zum Ziel lösen. Je kreativer und einleuchtender, desto besser. Gerne auch humorvoll, gerne einfach anders.

```html
<!DOCTYPE html>
<html lang="de">
<head>
<meta charset="utf-8">
<title>tkb – Gatefold-Flyer</title>
<link rel="stylesheet" href="https://fonts.googleapis.com/css2?family=Lato:ital,wght@0,300;0,400;0,700;0,900;1,300;1,700&display=swap">
<style>
  :root {
    --navy: #2c3580;
    --navy-deep: #242c6e;
    --paper: #ffffff;
    --backdrop: #e8e9ee;
    --ink-grey: #5a5d6a;
    --icon-grey: #6b6e78;
    --rock: #c98a3c;
    --rock-dark: #8a5424;
    --sky: #9fc2e0;
  }
  * { box-sizing: border-box; margin: 0; padding: 0; }
  html, body { width: 1200px; height: 987px; overflow: hidden; }
  body {
    background: var(--backdrop);
    font-family: "Lato", sans-serif;
    position: relative;
  }

  /* ---------- outside spread ---------- */
  .cover {
    position: absolute; left: 40px; top: 110px;
    width: 520px; height: 760px;
    display: flex;
    box-shadow: 0 10px 30px rgba(0,0,0,.12);
  }
  .flap { position: relative; width: 260px; height: 100%; overflow: hidden; }
  .flap + .flap { border-left: 1px solid rgba(255,255,255,.6); }
  .photo {
    position: absolute; inset: 0;
    background: linear-gradient(180deg, var(--rock-dark) 0%, var(--rock) 22%, var(--sky) 30%, #d9e4ec 55%, #5f7fa3 66%, var(--rock) 76%, #a8692c 100%);
  }
  .flap--right .photo { background-position: 0 0; }

  .panel-box {
    position: absolute; background: var(--navy); color: #fff;
    padding: 22px 18px;
  }
  .panel-box--intro { left: 18px; top: 40px; width: 210px; height: 520px; }
  .panel-box--promise { left: 40px; top: 380px; width: 220px; height: 340px; padding: 30px 20px; }

  .intro-question { font-weight: 300; font-size: 21px; line-height: 1.15; }
  .intro-relief { font-weight: 900; font-size: 22px; margin: 10px 0 8px; }
  .intro-lead { font-weight: 300; font-size: 12px; margin-bottom: 8px; }
  .brand-inline { font-weight: 700; font-style: italic; }
  .benefits { list-style: none; }
  .benefits li {
    position: relative; padding-left: 22px;
    font-weight: 300; font-size: 12px; line-height: 1.2; margin-bottom: 9px;
  }
  .benefits li svg { position: absolute; left: 0; top: 2px; }

  .promise { font-weight: 300; font-size: 22px; line-height: 1.22; }
  .promise strong { font-weight: 900; }

  /* ---------- inside spread ---------- */
  .inside {
    position: absolute; left: 600px; top: 110px;
    width: 560px; height: 760px;
    display: flex; background: var(--paper);
    box-shadow: 0 10px 30px rgba(0,0,0,.12);
  }
  .inside-main { position: relative; width: 340px; height: 100%; }
  .inside-side { position: relative; width: 220px; height: 100%; border-left: 1px solid #e3e4ea; }

  .tools-head {
    background: var(--navy); color: #fff;
    margin-top: 60px; padding: 18px 22px;
    font-weight: 300; font-size: 15px; line-height: 1.3;
  }
  .tools-head strong { font-weight: 900; font-size: 17px; }

  .tools { list-style: none; margin: 34px 22px 0 22px; }
  .tools li {
    display: flex; align-items: center; gap: 14px;
    margin-bottom: 30px; font-size: 12px; line-height: 1.25;
    color: var(--ink-grey); font-weight: 300;
  }
  .tools li .tool-text { border-left: 1px solid var(--navy); padding-left: 12px; }
  .tools li strong { color: var(--navy); font-weight: 700; }
  .tools svg { flex: 0 0 28px; }

  .upgrade {
    position: absolute; left: 22px; bottom: 70px; right: 20px;
    color: var(--navy); font-size: 21px; line-height: 1.2; font-weight: 300;
  }
  .upgrade strong { font-weight: 900; }

  .brand {
    position: absolute; left: 22px; top: 30px;
    display: flex; align-items: center; gap: 8px;
    color: var(--navy); font-weight: 700; font-size: 24px;
  }
  .brand-dot { width: 14px; height: 14px; border-radius: 50%; background: var(--navy); }
  .side-band { position: absolute; left: 22px; top: 90px; width: 36px; height: 300px; background: var(--navy); }
  .side-claim {
    position: absolute; left: 76px; top: 100px; right: 16px;
    color: var(--navy); font-weight: 300; font-style: italic;
    font-size: 18px; line-height: 1.25;
  }
  .side-claim strong { font-weight: 700; }
  .rockets {
    position: absolute; left: 30px; top: 420px; width: 160px; height: 240px;
    border-radius: 8px;
    background: linear-gradient(160deg, var(--navy) 0%, #5a5f8f 55%, #8a8c96 100%);
    opacity: .9;
  }
</style>
</head>
<body>

<section class="cover" aria-label="Außenseite">
  <div class="flap flap--left">
    <div class="photo" role="img" aria-label="Foto: Kletterer unter einem Felsüberhang vor Meer und Abendhimmel"></div>
    <div class="panel-box panel-box--intro">
      <p class="intro-question">Sie stehen vor einem technologischen Problem?</p>
      <p class="intro-relief">Keine Sorge.</p>
      <p class="intro-lead"><span class="brand-inline">tkb</span> bietet mir:</p>
      <ul class="benefits">
        <li><svg width="12" height="10" viewBox="0 0 12 10"><path d="M1 5l3.5 3.5L11 1" stroke="#fff" stroke-width="2" fill="none"/></svg>...neue Technologien, Ersatzprodukte/ Ersatzstoffe</li>
        <li><svg width="12" height="10" viewBox="0 0 12 10"><path d="M1 5l3.5 3.5L11 1" stroke="#fff" stroke-width="2" fill="none"/></svg>...Ideen für Neuentwicklungen</li>
        <li><svg width="12" height="10" viewBox="0 0 12 10"><path d="M1 5l3.5 3.5L11 1" stroke="#fff" stroke-width="2" fill="none"/></svg>...Zugang zu neuen Märkten</li>
        <li><svg width="12" height="10" viewBox="0 0 12 10"><path d="M1 5l3.5 3.5L11 1" stroke="#fff" stroke-width="2" fill="none"/></svg>...ergänzendes Wissen</li>
        <li><svg width="12" height="10" viewBox="0 0 12 10"><path d="M1 5l3.5 3.5L11 1" stroke="#fff" stroke-width="2" fill="none"/></svg>...interne Prozess- und Ablaufverbesserungen</li>
        <li><svg width="12" height="10" viewBox="0 0 12 10"><path d="M1 5l3.5 3.5L11 1" stroke="#fff" stroke-width="2" fill="none"/></svg>...passende Partner zur Realisierung</li>
        <li><svg width="12" height="10" viewBox="0 0 12 10"><path d="M1 5l3.5 3.5L11 1" stroke="#fff" stroke-width="2" fill="none"/></svg>...ein Expertennetzwerk von über 600.000 Ansprechpartnern</li>
      </ul>
    </div>
  </div>
  <div class="flap flap--right">
    <div class="photo" role="img" aria-label="Foto: Fortsetzung der Felslandschaft mit Küste"></div>
    <div class="panel-box panel-box--promise">
      <p class="promise">Wir beseitigen Ihre <strong>Engpässe</strong> und sind Ihnen ein strategischer <strong>Partner</strong> von Beginn bis zum Ende Ihres Projekts.</p>
    </div>
  </div>
</section>

<section class="inside" aria-label="Innenseite">
  <div class="inside-main">
    <div class="tools-head">
      Die tkb übernimmt die <strong>Gesamtprojektleitung</strong> für Ihr Unternehmen und nutzt für Ihr Projekt passende Tools:
    </div>
    <ul class="tools">
      <li>
        <svg width="28" height="22" viewBox="0 0 28 22"><rect x="1" y="1" width="26" height="20" rx="2" fill="var(--icon-grey)"/><rect x="5" y="5" width="5" height="4" fill="#fff"/><rect x="12" y="5" width="5" height="4" fill="#fff"/><rect x="19" y="5" width="5" height="4" fill="#fff"/><rect x="5" y="12" width="19" height="2" fill="#fff"/></svg>
        <span class="tool-text"><strong>Patent- und Literatur</strong>recherchen</span>
      </li>
      <li>
        <svg width="28" height="22" viewBox="0 0 28 22"><rect x="2" y="2" width="24" height="14" fill="none" stroke="var(--icon-grey)" stroke-width="2"/><path d="M14 16v5M9 21h10" stroke="var(--icon-grey)" stroke-width="2"/><rect x="7" y="6" width="8" height="6" fill="var(--icon-grey)"/></svg>
        <span class="tool-text">Geographisch spezifische Projektausschreibungen und <strong>Netzwerkbefragungen</strong></span>
      </li>
      <li>
        <svg width="28" height="26" viewBox="0 0 28 26"><circle cx="14" cy="10" r="8" fill="var(--icon-grey)"/><rect x="10" y="19" width="8" height="5" fill="var(--icon-grey)"/></svg>
        <span class="tool-text">Individuelles <strong>Projektmanagement</strong></span>
      </li>
      <li>
        <svg width="28" height="26" viewBox="0 0 28 26"><rect x="3" y="2" width="22" height="22" rx="2" fill="var(--icon-grey)"/><path d="M8 9l3 3 6-6" stroke="#fff" stroke-width="2" fill="none"/><circle cx="18" cy="18" r="2.5" fill="#fff"/></svg>
        <span class="tool-text">Tests, Sprint, <strong>Validierung</strong></span>
      </li>
      <li>
        <svg width="28" height="26" viewBox="0 0 28 26"><rect x="3" y="2" width="22" height="22" rx="2" fill="var(--icon-grey)"/><rect x="7" y="15" width="3" height="5" fill="#fff"/><rect x="12" y="11" width="3" height="9" fill="#fff"/><rect x="17" y="7" width="3" height="13" fill="#fff"/></svg>
        <span class="tool-text">Professionelle <strong>Marktanalyse</strong> und Technologieauswertung</span>
      </li>
    </ul>
    <p class="upgrade"><strong>Unternehmensupgrade</strong> durch technologische Beratung</p>
  </div>
  <div class="inside-side">
    <div class="brand"><span class="brand-dot"></span>tkb</div>
    <div class="side-band"></div>
    <p class="side-claim">Wir <strong>lösen</strong> Ihre unternehmerischen <strong>Probleme</strong> durch unser Wissen und unsere Tools.</p>
    <div class="rockets" role="img" aria-label="Illustration: drei startende Raketen in Blau und Grau"></div>
  </div>
</section>

</body>
</html>
```